LinkedIn Cover Image

We need a Linked In Cover Image for our Linked In Business Page.

The dimensions needed are: 1536 x 768px.

Here's a link to our website: www.harborvalerepair.com
LinkedIn Profile: https://www.linkedin.com/company/harborvale-repair-services/

Font styles to use
Sans Serif

Colors

Designer to choose colors to be used in the design.

```html
<!DOCTYPE html>
<html lang="en">
<head>
<meta charset="utf-8">
<title>Harborvale Repair Services – LinkedIn Cover</title>
<link href="https://fonts.googleapis.com/css2?family=Open+Sans:wdth,wght@75..100,400..800&display=swap" rel="stylesheet">
<style>
  :root {
    --backdrop: #dcdcdc;
    --paper: #ffffff;
    --orange: #f08c2a;
    --teal: #3e6b7b;
    --ink: #3d3d3d;
    --rule: #c9c9c9;
    --star-fill: #e7e8ea;
  }
  * { box-sizing: border-box; margin: 0; padding: 0; }
  html, body {
    width: 1200px; height: 900px; overflow: hidden;
    background: var(--backdrop);
    font-family: "Open Sans", Arial, sans-serif;
  }
  .cover {
    position: absolute; left: 76px; top: 170px;
    width: 1055px; height: 527px;
    background: var(--paper);
    overflow: hidden;
  }
  .header-art { position: absolute; left: 0; top: 0; }
  .brand {
    position: absolute; left: 30px; top: 26px;
    color: var(--orange); font-weight: 800;
    font-stretch: 85%;
    line-height: 1;
  }
  .brand-name { display: block; font-size: 96px; letter-spacing: 1px; }
  .brand-tagline { display: block; font-size: 38px; letter-spacing: 2px; margin-top: 10px; }
  .emergency {
    position: absolute; left: 652px; top: 28px;
    color: var(--paper);
  }
  .emergency-label { display: block; font-size: 36px; font-weight: 500; line-height: 1.1; }
  .emergency-number { display: block; font-size: 60px; font-weight: 500; line-height: 1.05; letter-spacing: -0.5px; margin-left: -6px; }
  .social {
    position: absolute; left: 754px; top: 170px;
    display: flex; gap: 8px; list-style: none;
  }
  .social li { width: 36px; height: 36px; border-radius: 50%; background: var(--paper); }
  .services {
    position: absolute; left: 120px; top: 243px;
    display: flex; list-style: none;
  }
  .service {
    width: 204px; text-align: center;
    color: var(--ink);
    font-weight: 600; font-stretch: 78%;
    font-size: 18px; line-height: 27px;
    position: relative;
  }
  .service + .service::before {
    content: ""; position: absolute; left: 0; top: 15px;
    width: 2px; height: 138px; background: var(--rule);
  }
  .service svg { display: block; margin: 0 auto 16px; }
  .site {
    position: absolute; left: 29px; right: 29px; top: 470px;
    display: flex; align-items: center; gap: 12px;
  }
  .site::before, .site::after {
    content: ""; flex: 1; height: 3px; background: var(--teal);
  }
  .site-url {
    font-size: 31px; font-weight: 700; color: var(--teal);
    letter-spacing: 0.3px;
  }
  .site-url .domain { color: var(--orange); }
</style>
</head>
<body>
<main class="cover">
  <svg class="header-art" width="1055" height="220" viewBox="0 0 1055 220" aria-hidden="true">
    <polygon points="627,0 1055,0 1055,153 596,153" fill="var(--teal)"/>
    <polygon points="594,161 1055,161 1055,217 589,217" fill="var(--orange)"/>
    <rect x="0" y="210" width="600" height="7" fill="var(--orange)"/>
  </svg>

  <h1 class="brand">
    <span class="brand-name">HARBORVALE</span>
    <span class="brand-tagline">REPAIR SERVICES</span>
  </h1>

  <p class="emergency">
    <span class="emergency-label">Emergency Line:</span>
    <span class="emergency-number">877-555-0142</span>
  </p>

  <ul class="social" aria-label="Social profiles">
    <li></li><li></li><li></li><li></li>
  </ul>

  <ul class="services">
    <li class="service">
      <svg width="142" height="142" viewBox="0 0 142 142" aria-hidden="true">
        <circle cx="71" cy="71" r="66" fill="none" stroke="var(--orange)" stroke-width="7"/>
        <circle cx="71" cy="71" r="60" fill="none" stroke="var(--rule)" stroke-width="1.5"/>
        <path d="M71 25 C64 50 48 68 48 88 A23 23 0 0 0 94 88 C94 68 78 50 71 25 Z" fill="var(--orange)"/>
        <path d="M72 55 C68 68 62 76 62 86 A10 10 0 0 0 82 86 C82 76 76 68 72 55 Z" fill="#f6b46c"/>
      </svg>
      WATER AND FLOOD<br>RESTORATION
    </li>
    <li class="service">
      <svg width="142" height="142" viewBox="0 0 142 142" aria-hidden="true">
        <circle cx="71" cy="71" r="66" fill="none" stroke="var(--orange)" stroke-width="7"/>
        <circle cx="71" cy="71" r="60" fill="none" stroke="var(--rule)" stroke-width="1.5"/>
        <path d="M68 22 C74 40 58 50 48 72 C40 92 52 114 71 114 C92 114 102 96 96 76 C93 66 86 60 86 50 C80 58 80 64 78 68 C78 50 76 34 68 22 Z" fill="var(--orange)"/>
        <path d="M72 78 C66 88 62 94 62 101 A10 10 0 0 0 82 101 C82 94 78 88 72 78 Z" fill="#f6b46c"/>
      </svg>
      FIRE AND SMOKE<br>RESTORATION
    </li>
    <li class="service">
      <svg width="142" height="142" viewBox="0 0 142 142" aria-hidden="true">
        <circle cx="71" cy="71" r="66" fill="none" stroke="var(--orange)" stroke-width="7"/>
        <circle cx="71" cy="71" r="60" fill="none" stroke="var(--rule)" stroke-width="1.5"/>
        <path d="M56 62 Q71 52 86 62 L90 94 Q71 110 52 94 Z" fill="var(--orange)"/>
        <rect x="30" y="76" width="26" height="32" rx="9" fill="var(--orange)"/>
        <rect x="86" y="76" width="26" height="32" rx="9" fill="var(--orange)"/>
        <rect x="35" y="82" width="16" height="20" rx="5" fill="#fde3c6"/>
        <rect x="91" y="82" width="16" height="20" rx="5" fill="#fde3c6"/>
      </svg>
      MOLD<br>REMEDIATION
    </li>
    <li class="service">
      <svg width="142" height="142" viewBox="0 0 142 142" aria-hidden="true">
        <circle cx="71" cy="71" r="66" fill="var(--star-fill)" stroke="var(--orange)" stroke-width="7"/>
        <circle cx="71" cy="71" r="60" fill="none" stroke="var(--rule)" stroke-width="1.5"/>
        <polygon points="71,20 83,57 122,57 90,80 102,118 71,95 40,118 52,80 20,57 59,57" fill="var(--paper)" stroke="var(--orange)" stroke-width="1.2"/>
      </svg>
      SPECIALTY<br>SERVICES
    </li>
  </ul>

  <p class="site">
    <span class="site-url">www.<span class="domain">harborvalerepair</span>.com</span>
  </p>
</main>
</body>
</html>
```